Marisol Specialty Coffee needs a Packaging design

We need packaging design for coffee that suits our brand identity, that is the best quality in Mexico.
We only sell mexican coffee with Q scores above 80
We are evaluating 3 types of packaging: Bag, Box and Cillinder can
The specific package format will be decided based on the designs that we get.
Updates

Target Market(s)

Coffee experts and enthusiast.
People that relate the Coffee consumption and experience with wine tasting and Bon Vivant way

Requirements
Should not have
• Photos any mexican cliché

```html
<!DOCTYPE html>
<html lang="en">
<head>
<meta charset="utf-8">
<title>Marisol Specialty Coffee – Packaging</title>
<link href="https://fonts.googleapis.com/css2?family=Libre+Baskerville:wght@700&display=swap" rel="stylesheet">
<style>
  :root {
    --gold: #b7862c;
    --black: #000000;
    --white: #ffffff;
    --paper: #ffffff;
  }
  html, body {
    margin: 0;
    padding: 0;
    width: 1200px;
    height: 1000px;
    overflow: hidden;
    background: var(--paper);
  }
  .canvas {
    position: relative;
    width: 1200px;
    height: 1000px;
    background: var(--paper);
  }
  .package-wrap {
    position: absolute;
    left: 12px;
    top: 174px;
    width: 1181px;
    height: 641px;
  }
  .pattern-gold {
    position: absolute;
    left: 0;
    top: 0;
    width: 436px;
    height: 641px;
    background: repeating-linear-gradient(180deg, var(--gold) 0 65px, #5c431a 65px 129px);
  }
  .front-panel {
    position: absolute;
    left: 436px;
    top: 0;
    width: 590px;
    height: 641px;
    background: var(--black);
  }
  .side-strip {
    position: absolute;
    left: 1026px;
    top: 0;
    width: 155px;
    height: 641px;
    background: var(--gold);
  }
  .brand {
    position: absolute;
    left: 178px;
    top: 68px;
    display: flex;
    align-items: center;
    gap: 16px;
  }
  .brand-dot {
    width: 44px;
    height: 44px;
    border-radius: 50%;
    background: var(--gold);
  }
  .brand-name {
    font-family: "Libre Baskerville", "Times New Roman", serif;
    font-weight: 700;
    font-size: 26px;
    color: var(--gold);
    letter-spacing: 0.5px;
    white-space: nowrap;
  }
  .pattern-mono {
    position: absolute;
    left: 155px;
    top: 188px;
    width: 435px;
    height: 453px;
    background: repeating-linear-gradient(180deg, #ffffff 0 33px, #1a1a1a 33px 66px);
  }
  .quality-ribbon {
    position: absolute;
    left: 813px;
    top: 553px;
    width: 213px;
    height: 53px;
  }
  .quality-ribbon svg {
    position: absolute;
    inset: 0;
  }
  .quality-label {
    position: absolute;
    left: 40px;
    right: 0;
    top: 0;
    height: 53px;
    line-height: 53px;
    text-align: center;
    font-family: "Libre Baskerville", "Times New Roman", serif;
    font-weight: 700;
    font-size: 15px;
    color: var(--white);
    letter-spacing: 0.3px;
  }
</style>
</head>
<body>
  <div class="canvas">
    <div class="package-wrap">
      <div class="pattern-gold" role="img" aria-label="Repeating black linked-loop pattern on gold"></div>
      <div class="front-panel">
        <div class="brand">
          <span class="brand-dot"></span>
          <span class="brand-name">Marisol Specialty Coffee</span>
        </div>
        <div class="pattern-mono" role="img" aria-label="Repeating black linked-loop pattern on white"></div>
      </div>
      <div class="side-strip"></div>
      <div class="quality-ribbon">
        <svg width="213" height="53" viewBox="0 0 213 53" aria-hidden="true">
          <polygon points="0,0 213,0 213,53 0,53 27,26.5" fill="var(--gold)"/>
        </svg>
        <div class="quality-label">BEST QUALITY</div>
      </div>
    </div>
  </div>
</body>
</html>
```